New corporate stationery design for UK train leasing company

In advance of an office move later this year we are looking to redesign all our corporate stationery (business cards, letterhead, compliment slips, envelopes etc) as well as small branded items (such as mouse mats, drink mats, etc).

We wish to keep the same logo and corporate colours but are looking for a modern, fresh look that will tie in our stationery more with the look of our website and our PowerPoint template. We have a strapline, "Track Crews, True Knowhow" that we would like to incorporate into the stationery design and also need to include a "TEMLO" logo on the bottom of the letterhead/compliment slips. We have two offices so will need letterhead and compliment slips with both addresses.

The files attached include different versions of our logo (the main one is the black with green halo, file 1 or 3), our brand guidelines summary (including Pantone colours), the TEMLO logo and PowerPoint template.

More information about the business can be found at www.fernholtrail.co.uk.

If you have any questions please let me know.

I look forward to seeing the designs!
Regards
Moira

Target Market(s)

Main audience are train operators, rail industry suppliers, passenger transport groups, government and other political organisations, financiers/lenders.

Industry/Entity Type

Business

```html
<!DOCTYPE html>
<html lang="en">
<head>
<meta charset="utf-8">
<title>Fernhol Stationery Set</title>
<link href="https://fonts.googleapis.com/css2?family=Open+Sans:wght@300;400;600;700&display=swap" rel="stylesheet">
<style>
  :root {
    --teal: #17a88c;
    --teal-light: #5cc7b2;
    --ink: #5f6468;
    --navy: #1d2a4a;
    --paper: #ffffff;
    --board: #cfd0d2;
    --line: #d9dcdd;
  }
  * { margin: 0; padding: 0; box-sizing: border-box; }
  html, body { width: 900px; height: 1200px; overflow: hidden; }
  body { background: var(--board); font-family: "Open Sans", sans-serif; color: var(--ink); position: relative; }
  .sheet { position: absolute; box-shadow: 0 2px 6px rgba(0,0,0,.18); overflow: hidden; }

  .wordmark { font-family: "Open Sans", sans-serif; font-weight: 300; color: var(--ink); letter-spacing: .5px; line-height: 1; }
  .wordmark.light { color: var(--paper); }
  .tagline { font-weight: 600; color: var(--teal); line-height: 1.2; }
  .tagline.light { color: var(--paper); }
  .partner { position: absolute; font-weight: 700; color: var(--navy); letter-spacing: .5px; }
  .contact { position: absolute; font-size: 6px; line-height: 1.45; color: var(--ink); }
  .contact b { font-weight: 600; color: var(--teal); }
  .band { position: absolute; left: 0; width: 100%; }

  /* Letterhead */
  .letterhead { left: 45px; top: 30px; width: 411px; height: 699px; background: var(--paper); }
  .letterhead .wordmark { position: absolute; left: 30px; top: 30px; font-size: 30px; }
  .letterhead .tagline { position: absolute; left: 30px; top: 68px; font-size: 8px; }
  .letterhead .band { bottom: 30px; height: 28px; }
  .letterhead .partner { right: 14px; bottom: 36px; font-size: 15px; }
  .letterhead .contact { left: 12px; bottom: 4px; }

  /* Letterhead reverse */
  .reverse { left: 474px; top: 30px; width: 396px; height: 699px; background: var(--teal); }
  .reverse .lockup { position: absolute; left: 0; right: 0; top: 270px; text-align: center; }
  .reverse .wordmark { font-size: 40px; }
  .reverse .tagline { font-size: 9px; margin-top: 6px; }

  /* Business cards */
  .card-front { left: 45px; top: 753px; width: 180px; height: 57px; background: var(--paper); }
  .card-front .wordmark { position: absolute; left: 10px; top: 8px; font-size: 13px; }
  .card-front .contact { left: 100px; top: 10px; font-size: 4.5px; text-align: right; right: 8px; left: auto; }
  .card-front .band { bottom: 0; height: 8px; }
  .card-back { left: 240px; top: 753px; width: 216px; height: 57px; background: var(--teal); }
  .card-back .label { position: absolute; right: 10px; top: 6px; font-size: 5px; color: var(--navy); font-weight: 600; text-align: right; line-height: 1.3; }
  .card-back .lockup { position: absolute; left: 0; right: 0; top: 20px; text-align: center; }
  .card-back .wordmark { font-size: 16px; }
  .card-back .tagline { font-size: 4.5px; margin-top: 2px; }

  /* Envelope */
  .envelope { left: 24px; top: 816px; width: 432px; height: 249px; background: var(--paper); }
  .envelope svg { position: absolute; left: 0; top: 0; }

  /* Compliment slip */
  .slip { left: 141px; top: 966px; width: 444px; height: 165px; background: var(--paper); box-shadow: 0 3px 8px rgba(0,0,0,.25); }
  .slip .wordmark { position: absolute; left: 22px; top: 16px; font-size: 22px; }
  .slip .tagline { position: absolute; left: 22px; top: 44px; font-size: 6px; }
  .slip .greeting { position: absolute; left: 22px; top: 60px; font-size: 7px; font-style: italic; color: var(--ink); }
  .slip .band { bottom: 22px; height: 24px; }
  .slip .partner { right: 12px; bottom: 26px; font-size: 12px; }
  .slip .contact { left: 12px; bottom: 2px; font-size: 5px; }
</style>
</head>
<body>

  <section class="sheet letterhead">
    <div class="wordmark">fernhol</div>
    <div class="tagline">Track Crews, True Knowhow</div>
    <svg class="band" viewBox="0 0 411 28" preserveAspectRatio="none" aria-hidden="true">
      <polygon points="0,6 240,6 262,28 0,28" fill="var(--teal)"/>
      <polygon points="262,28 240,6 411,6 411,8 244,8 264,28" fill="var(--teal-light)"/>
    </svg>
    <div class="partner">TEMLO</div>
    <div class="contact">
      <b>Fernhol Trains Ltd</b><br>
      12 Wharf Lane, London SE1 4QT<br>
      4 Mill Street, Derby DE1 2RT<br>
      T 020 7946 0312 &nbsp; www.fernholtrail.co.uk
    </div>
  </section>

  <section class="sheet reverse">
    <div class="lockup">
      <div class="wordmark light">fernhol</div>
      <div class="tagline light">Track Crews, True Knowhow</div>
    </div>
  </section>

  <section class="sheet card-front">
    <div class="wordmark">fernhol</div>
    <div class="contact">
      <b>Moira Dean</b><br>
      Office Manager<br>
      T 020 7946 0312<br>
      moira@fernholtrail.co.uk
    </div>
    <svg class="band" viewBox="0 0 180 8" preserveAspectRatio="none" aria-hidden="true">
      <polygon points="0,0 110,0 118,8 0,8" fill="var(--teal)"/>
    </svg>
  </section>

  <section class="sheet card-back">
    <div class="label">Moira Dean<br>Office Manager</div>
    <div class="lockup">
      <div class="wordmark light">fernhol</div>
      <div class="tagline light">Track Crews, True Knowhow</div>
    </div>
  </section>

  <section class="sheet envelope">
    <svg width="432" height="249" viewBox="0 0 432 249" aria-hidden="true">
      <polyline points="0,0 216,95 432,0" fill="none" stroke="var(--line)" stroke-width="1.5"/>
      <polygon points="0,120 180,120 205,150 0,150" fill="var(--teal)"/>
    </svg>
  </section>

  <section class="sheet slip">
    <div class="wordmark">fernhol</div>
    <div class="tagline">Track Crews, True Knowhow</div>
    <div class="greeting">With compliments</div>
    <svg class="band" viewBox="0 0 444 24" preserveAspectRatio="none" aria-hidden="true">
      <polygon points="0,4 250,4 270,24 0,24" fill="var(--teal)"/>
      <polygon points="270,24 250,4 444,4 444,6 253,6 272,24" fill="var(--teal-light)"/>
    </svg>
    <div class="partner">TEMLO</div>
    <div class="contact">
      <b>Fernhol Trains Ltd</b> &nbsp; 12 Wharf Lane, London SE1 4QT &nbsp; www.fernholtrail.co.uk
    </div>
  </section>

</body>
</html>
```